New Business Card for Software Company

We are looking at rebranding a 10 year old company that specializes in PDF and DWF solutions for Architects and Engineers. We will attach the new company logo that we are going with so you can work with that and complimentary colors.
The sample information we would like on the business card is:
Gerald Pembrook
Vice President
4173 W. Tillman Avenue. STE 306
PMB#417
Calder, NM 85316
866-392-7154 US Toll Free
123-581-3064 Cell
gpembrook@vextrolan.com
The old tag line that we had on the business cars was.
Delivering Dependable Drawing and Document Tools to Design Teams Everywhere.
If you have an idea for a better tag line we are open to that also.
Updates
We would like to thank all of the Designers for their wonderful work. We apologize that we will not have the time to provide feedback to everyone. There is just so many innovative and professional designs that you have all created making our decision even harder.
Target Market(s)
Architects and Engineers
Industry/Entity Type
Business
Look and feel
Each slider illustrates characteristics of the customer's brand and the style your logo design should communicate.

```html
<!DOCTYPE html>
<html lang="en">
<head>
<meta charset="utf-8">
<title>Vextrolan Business Card</title>
<link href="https://fonts.googleapis.com/css2?family=Barlow:wght@400;500;700;800&display=swap" rel="stylesheet">
<style>
  :root {
    --bg: #e9e6e1;
    --orange: #f08a1c;
    --orange-deep: #e06a12;
    --amber: #f2a72a;
    --red-orange: #d9481e;
    --wine: #9c4a4e;
    --peach: #f3b07a;
    --ink: #5b5b5d;
    --card-white: #f4f4f3;
  }
  * { margin: 0; padding: 0; box-sizing: border-box; }
  html, body { width: 1200px; height: 900px; overflow: hidden; }
  body {
    background: var(--bg);
    font-family: "Barlow", Arial, sans-serif;
    position: relative;
  }
  .card {
    position: absolute;
    left: 250px;
    width: 700px;
    height: 400px;
    overflow: hidden;
    box-shadow: 0 6px 18px rgba(0,0,0,0.15);
  }
  .card-front {
    top: 33px;
    background: linear-gradient(135deg, var(--amber) 0%, var(--orange) 55%, var(--orange-deep) 100%);
  }
  .card-back {
    top: 467px;
    background: var(--card-white);
  }
  .brand-decoration {
    position: absolute;
    right: 0;
    top: 0;
    width: 220px;
    height: 160px;
    background: radial-gradient(ellipse at 60% 30%, rgba(217,72,30,0.45), rgba(217,72,30,0) 70%);
  }
  .wordmark {
    display: flex;
    align-items: center;
    gap: 14px;
    position: absolute;
  }
  .wordmark-dot {
    border-radius: 50%;
    background: var(--red-orange);
  }
  .wordmark-name {
    font-weight: 800;
    letter-spacing: -1px;
    line-height: 1;
  }
  .card-front .wordmark { left: 90px; top: 150px; }
  .card-front .wordmark-dot { width: 64px; height: 64px; }
  .card-front .wordmark-name { font-size: 78px; color: var(--red-orange); }
  .tagline {
    position: absolute;
    left: 190px;
    top: 268px;
    width: 420px;
    color: #fff3e4;
    font-size: 20px;
    font-weight: 500;
    text-align: center;
    line-height: 1.3;
  }
  .swoosh-illustration {
    position: absolute;
    left: 0;
    bottom: 0;
    width: 290px;
    height: 400px;
    background: linear-gradient(160deg, var(--wine) 0%, var(--peach) 45%, var(--amber) 100%);
    clip-path: polygon(0 40%, 30% 0, 70% 0, 100% 100%, 0 100%);
  }
  .card-back .wordmark { left: 300px; top: 60px; }
  .card-back .wordmark-dot { width: 54px; height: 54px; }
  .card-back .wordmark-name { font-size: 64px; color: var(--red-orange); }
  .person {
    position: absolute;
    left: 370px;
    top: 150px;
  }
  .person-name {
    color: var(--red-orange);
    font-size: 26px;
    font-weight: 500;
    text-transform: uppercase;
    letter-spacing: 0.5px;
  }
  .person-title {
    color: var(--ink);
    font-size: 20px;
    margin-top: 2px;
  }
  .contact {
    list-style: none;
    margin-top: 16px;
    color: var(--ink);
    font-size: 17px;
    line-height: 1.45;
  }
  .contact-label {
    display: inline-block;
    width: 20px;
    color: var(--red-orange);
    font-weight: 700;
  }
  .address {
    margin-top: 6px;
    padding-left: 20px;
    color: var(--ink);
    font-size: 17px;
    line-height: 1.45;
    font-style: normal;
  }
</style>
</head>
<body>
  <section class="card card-front" aria-label="Business card front">
    <div class="brand-decoration" role="img" aria-label="Soft brand colour accent"></div>
    <div class="wordmark">
      <span class="wordmark-dot"></span>
      <span class="wordmark-name">Vextrolan</span>
    </div>
    <p class="tagline">Delivering Dependable Drawing and Document Tools to Design Teams Everywhere</p>
  </section>

  <section class="card card-back" aria-label="Business card back">
    <div class="swoosh-illustration" role="img" aria-label="Abstract orange and plum ribbon illustration"></div>
    <div class="wordmark">
      <span class="wordmark-dot"></span>
      <span class="wordmark-name">Vextrolan</span>
    </div>
    <div class="person">
      <h1 class="person-name">Gerald Pembrook</h1>
      <p class="person-title">Vice President</p>
      <ul class="contact">
        <li><span class="contact-label">T</span>866-392-7154 US Toll Free</li>
        <li><span class="contact-label">M</span>123-581-3064</li>
        <li><span class="contact-label">E</span>gpembrook@vextrolan.com</li>
      </ul>
      <address class="address">4173 W. Tillman Avenue. STE 306,<br>PMB#417, Calder, NM 85316</address>
    </div>
  </section>
</body>
</html>
```